KL MOTORS BANNER/SIGN DESIGN

Design a banner sign for outdoor use for KL MOTORS - a premium pre owned vehicle sales center. The size must be 36 feet in width
and 3 feet in height.

Information required: logo (attached)
-PREMIUM PRE-OWEND VEHICLE SALES
- 517.264.3081

perhaps in smaller font: BUY-SELL-TRADE

prefer white background but could possibly do red matching the logo

```html
<!DOCTYPE html>
<html lang="en">
<head>
<meta charset="utf-8">
<title>KL Motors Banner</title>
<link rel="stylesheet" href="https://fonts.googleapis.com/css2?family=Montserrat:wght@700;800&display=swap">
<style>
  :root {
    --backdrop: #b5b5b5;
    --banner-white: #ffffff;
    --brand-red: #de1f26;
    --ink-black: #0d0d0d;
    --text-white: #ffffff;
  }
  * { margin: 0; padding: 0; box-sizing: border-box; }
  html, body {
    width: 1200px;
    height: 518px;
    overflow: hidden;
    background: var(--backdrop);
    font-family: "Montserrat", Arial, sans-serif;
  }
  .banner {
    position: absolute;
    left: 89px;
    top: 214px;
    width: 1022px;
    height: 85px;
    background: var(--banner-white);
    overflow: hidden;
  }
  .banner-shapes {
    position: absolute;
    inset: 0;
  }
  .brand {
    position: absolute;
    left: 23px;
    top: 12px;
    height: 60px;
    display: flex;
    align-items: center;
    gap: 14px;
  }
  .brand-dot {
    width: 46px;
    height: 46px;
    border-radius: 50%;
    background: var(--brand-red);
  }
  .brand-name {
    font-weight: 800;
    font-size: 27px;
    letter-spacing: 1px;
    color: var(--ink-black);
    white-space: nowrap;
  }
  .headline {
    position: absolute;
    left: 364px;
    width: 502px;
    top: 9px;
    text-align: center;
    font-weight: 800;
    font-size: 22.5px;
    color: var(--ink-black);
    white-space: nowrap;
  }
  .headline .accent { color: var(--brand-red); }
  .phone {
    position: absolute;
    left: 481px;
    width: 266px;
    top: 41px;
    height: 29px;
    display: flex;
    align-items: center;
    justify-content: center;
    gap: 8px;
    color: var(--text-white);
    font-weight: 800;
    font-size: 24px;
    letter-spacing: 0.3px;
  }
  .phone-icon { width: 18px; height: 18px; }
  .services {
    position: absolute;
    left: 915px;
    top: 11px;
    list-style: none;
    color: var(--text-white);
    font-weight: 800;
    font-size: 18px;
    line-height: 21px;
  }
  .services li::before {
    content: "";
    display: inline-block;
    width: 7px;
    height: 7px;
    border-radius: 50%;
    background: var(--text-white);
    margin-right: 6px;
    vertical-align: 3px;
  }
</style>
</head>
<body>
  <div class="banner">
    <svg class="banner-shapes" width="1022" height="85" viewBox="0 0 1022 85" aria-hidden="true">
      <polygon points="298,0 335,0 315,50" fill="var(--brand-red)"/>
      <polygon points="347,0 356,0 312,85 303,85" fill="var(--ink-black)"/>
      <polygon points="486,41 754,41 745,70 477,70" fill="var(--brand-red)"/>
      <polygon points="467,41 477,41 472,50" fill="var(--ink-black)"/>
      <polygon points="755,70 765,70 760,60" fill="var(--ink-black)"/>
      <polygon points="906,0 912,0 912,85 862,85" fill="var(--brand-red)"/>
      <polygon points="912,0 1022,0 1022,85 885,85" fill="var(--ink-black)"/>
    </svg>

    <div class="brand">
      <span class="brand-dot"></span>
      <span class="brand-name">KL MOTORS</span>
    </div>

    <p class="headline">PREMIUM <span class="accent">PRE-OWNED</span> VEHICLE SALES</p>

    <div class="phone">
      <svg class="phone-icon" viewBox="0 0 24 24" aria-hidden="true">
        <path fill="var(--text-white)" d="M6.6 10.8a15.1 15.1 0 0 0 6.6 6.6l2.2-2.2a1 1 0 0 1 1-.25 11.4 11.4 0 0 0 3.6.57 1 1 0 0 1 1 1V20a1 1 0 0 1-1 1A17 17 0 0 1 3 4a1 1 0 0 1 1-1h3.5a1 1 0 0 1 1 1c0 1.25.2 2.45.57 3.57a1 1 0 0 1-.25 1z"/>
        <path fill="none" stroke="var(--text-white)" stroke-width="1.8" stroke-linecap="round" d="M14 3.5a7 7 0 0 1 6.5 6.5M14 7a3.5 3.5 0 0 1 3 3"/>
      </svg>
      <span class="phone-number">517.264.3081</span>
    </div>

    <ul class="services">
      <li>BUY</li>
      <li>SELL</li>
      <li>TRADE</li>
    </ul>
  </div>
</body>
</html>
```